I need a label design to go on our jars of honey. Our company is called Quillbrook Honey Co. The type of honey is called Marram Glade Honey. The jars are 1kg. Attached is the label size. Left hand side needs to have nutritional info... as attached. Middle section is our company name, honey type, 1kg & Whangamata, NZ. Right hand side needs to have info as per photo (raw honey etc). I would like to upload more pictures... but I’m unsure how to do this? Thanks, Noreen

Target Market(s)

Honey consumers... families

Industry/Entity Type

Food Production

Colors

Designer to choose colors to be used in the design.

Requirements
Must have
• Nutritional info as per upload
• Type of honey & company name as per upload
• 1kg
• Address
Nice to have
• Similar fonts to upload.
• Possibly background image... floral or beach... very faint though.

```html
<!DOCTYPE html>
<html lang="en">
<head>
<meta charset="utf-8">
<title>Quillbrook Honey Co. – Marram Glade Honey Label</title>
<link href="https://fonts.googleapis.com/css2?family=Itim&family=Oswald:wght@300;400&family=Kaushan+Script&family=Roboto+Condensed:wght@400;700&display=swap" rel="stylesheet">
<style>
  :root {
    --page: #ffffff;
    --rose: #dc7384;
    --rose-light: #e993a0;
    --rose-deep: #c95d6f;
    --sea: #e7808a;
    --island: #b9505f;
    --ink: #ffffff;
    --ink-dark: #2a1a1d;
    --field: rgba(255, 235, 240, 0.88);
  }
  * { box-sizing: border-box; margin: 0; padding: 0; }
  html, body {
    width: 1182px; height: 1200px; overflow: hidden;
    background: var(--page);
  }
  .label {
    position: absolute; left: 29px; top: 376px;
    width: 1124px; height: 448px; overflow: hidden;
    color: var(--ink);
    font-family: "Itim", cursive;
  }
  .label__backdrop {
    position: absolute; inset: 0;
    background:
      radial-gradient(ellipse at 12% 20%, var(--rose-light) 0%, transparent 45%),
      radial-gradient(ellipse at 88% 22%, var(--rose-light) 0%, transparent 45%),
      radial-gradient(ellipse at 50% 35%, #e68a99 0%, transparent 40%),
      var(--rose);
  }
  .label__shore {
    position: absolute; left: 0; right: 0; bottom: 0; height: 70px;
    background: linear-gradient(var(--rose-deep), var(--sea));
    opacity: 0.55;
  }
  .label__shore svg { position: absolute; inset: 0; }

  /* left panel */
  .facts { position: absolute; left: 46px; top: 30px; width: 240px; text-align: center; }
  .facts__claim { font-size: 17px; line-height: 25px; }
  .nutrition {
    margin: 20px 0 0 8px; width: 216px;
    border: 2px solid var(--ink);
    font-family: "Roboto Condensed", sans-serif;
    font-size: 8px; border-collapse: collapse; text-align: left;
  }
  .nutrition th { font-weight: 400; padding: 3px 4px; border-bottom: 1px solid var(--ink); }
  .nutrition .sub th { border-right: 1px solid var(--ink); font-size: 7px; }
  .nutrition .sub th:last-child { border-right: 0; }
  .nutrition td { font-size: 10.5px; padding: 2px 8px; border-bottom: 1px solid var(--ink); }
  .nutrition tr:last-child td { border-bottom: 0; }
  .nutrition td + td { text-align: right; padding: 2px 6px; }
  .facts__care { margin-top: 12px; font-size: 14px; line-height: 19px; }
  .batch {
    position: absolute; left: 46px; top: 364px; width: 234px; height: 61px;
    background: var(--field); color: var(--ink-dark);
    font-family: "Roboto Condensed", sans-serif; font-weight: 700; font-size: 11px;
    padding: 6px 8px; line-height: 18px;
  }
  .batch span { display: inline-block; width: 62px; }

  /* centre panel */
  .brand { position: absolute; left: 362px; width: 400px; text-align: center; font-family: "Oswald", sans-serif; font-weight: 300; }
  .brand__name { top: 32px; font-size: 44px; letter-spacing: 12px; line-height: 50px; text-transform: uppercase; padding-left: 12px; }
  .brand__sub { top: 88px; font-size: 19px; letter-spacing: 9px; text-transform: uppercase; padding-left: 9px; }
  .product { position: absolute; left: 262px; width: 600px; text-align: center; font-family: "Kaushan Script", cursive; line-height: 1; }
  .product__type { top: 168px; font-size: 64px; }
  .product__kind { top: 256px; font-size: 72px; }
  .weight { position: absolute; left: 462px; width: 200px; top: 344px; text-align: center; font-family: "Oswald", sans-serif; font-weight: 300; font-size: 28px; }
  .origin { position: absolute; left: 412px; width: 300px; top: 404px; text-align: center; font-family: "Oswald", sans-serif; font-weight: 400; font-size: 16px; letter-spacing: 0.5px; }

  /* right panel */
  .story { position: absolute; left: 820px; width: 280px; top: 66px; text-align: center; font-size: 14px; line-height: 26.5px; }
  .story p + p { margin-top: 26px; }
</style>
</head>
<body>
  <section class="label">
    <div class="label__backdrop" role="img" aria-label="Faint watercolour roses and flowers across a soft pink background"></div>
    <div class="label__shore" role="img" aria-label="Faint beach horizon with small palm islands">
      <svg width="1124" height="70" viewBox="0 0 1124 70" preserveAspectRatio="none">
        <path d="M0 52 Q200 40 380 52 L380 70 L0 70Z" fill="var(--island)" opacity="0.35"/>
        <path d="M800 50 Q950 30 1124 48 L1124 70 L800 70Z" fill="var(--island)" opacity="0.35"/>
      </svg>
    </div>

    <div class="facts">
      <p class="facts__claim">100% New Zealand Honey<br>No added ingredients</p>
      <table class="nutrition">
        <tr><th colspan="2">NUTRITION INFORMATION</th><th style="text-align:right">NET WEIGHT 1000g</th></tr>
        <tr class="sub"><th>SERVINGS PER PACK: APPROX 17</th><th>PER SERVING</th><th>PER 100g</th></tr>
        <tr><td>ENERGY</td><td>134KJ</td><td>1400KJ</td></tr>
        <tr><td>PROTEIN</td><td>0.04g</td><td>0.4g</td></tr>
        <tr><td>FAT, TOTAL</td><td>0.0g</td><td>0.0g</td></tr>
        <tr><td>CARBOHYDRATE</td><td>7.9g</td><td>79.6g</td></tr>
        <tr><td>SUGARS</td><td>7.8g</td><td>78.8g</td></tr>
        <tr><td>SODIUM</td><td>1.2mg</td><td>12mg</td></tr>
      </table>
      <p class="facts__care">Store upright in a cool, dry place.<br>No refrigeration needed.<br>Not recommended for infants below<br>the age of 12 months.</p>
    </div>
    <div class="batch">
      <div><span>Best Before</span>:</div>
      <div><span>MRP</span>:</div>
      <div><span>Batch No</span>:</div>
    </div>

    <h1 class="brand brand__name">Quillbrook</h1>
    <p class="brand brand__sub">Honey Co.</p>
    <h2 class="product product__type">Marram Glade</h2>
    <p class="product product__kind">Honey</p>
    <p class="weight">1KG</p>
    <p class="origin">KOWHAI COVE N.Z.</p>

    <div class="story">
      <p>Sourced from the beautiful<br>Coromandel Peninsula.</p>
      <p>Our honey comes to you raw &amp;<br>unpasteurised, ensuring it retains<br>all the natural goodness!</p>
      <p>Arohanui,<br>Rowan, Noreen &amp; boys</p>
      <p>'Quillbrook' - all thanks to God for His<br>incredible creation!</p>
    </div>
  </section>
</body>
</html>
```